Marbeck Partners Exit Plan business consultant web site

This website is for a consulting business that helps other businesses with exit plans. Essentially, assists them with the sale of their business. This website should be very professional, almost with a wall street look. I would like a very attractive image on the homepage. Perhaps something that denotes success. Perhaps a picture of palm trees and a beach? I will leave it to you for interpretation.

Across the screen I would like the words "Does your business have an exit plan?"

Below that it should read the following:
Let us help you with a completely impartial, no obligation assessment (button with link to the contact page)

Also, please use logo in a prominent place on the website so it's easily seen.

Target Market(s)

Males 40+

Coding

Coded - Design and coding required

Number of Pages Required

5+ page

Colors

Designer to choose colors to be used in the design.

Requirements
Must have
• The tabs for the homepage on the top should be:
• 1. About us
• 2. Services
• 3. Industries
• 4. Our success
• 5. Contact
Nice to have
• Clean, professional image.
• Please put FB, Twitter, Linked In - logos at bottom.
• Here are two examples of a website to give you an idea:
• https://blog.trevanquill.com/library/why-every-business-owner-should-have-an-exit-plan
Should not have
• nothing whimsical or cartoon like

```html
<!DOCTYPE html>
<html lang="en">
<head>
<meta charset="utf-8">
<title>Marbeck Partners — Exit Planning Consultants</title>
<link rel="stylesheet" href="https://fonts.googleapis.com/css2?family=Cinzel:wght@400;600;700&family=Open+Sans:wght@400;600&display=swap">
<style>
  :root {
    --blue: #1e96d3;
    --ink: #111111;
    --text: #555555;
    --light: #f3f3f3;
    --white: #ffffff;
    --footer: #17171c;
    --line: #bdbdbd;
  }
  * { box-sizing: border-box; margin: 0; padding: 0; }
  html, body { width: 1200px; height: 4633px; overflow: hidden; }
  body { font-family: "Open Sans", Arial, sans-serif; color: var(--text); background: var(--white); position: relative; }
  .serif { font-family: "Cinzel", "Times New Roman", serif; }
  section, header, footer, .topbar { position: absolute; left: 0; width: 1200px; }
  .abs { position: absolute; }
  .btn { position: absolute; display: flex; align-items: center; justify-content: center; background: var(--ink); color: var(--white); font-family: "Cinzel", serif; font-weight: 600; text-decoration: none; letter-spacing: .5px; }

  .topbar { top: 0; height: 48px; background: var(--blue); color: var(--white); font-size: 16px; font-weight: 600; }
  .topbar .item { position: absolute; top: 13px; display: flex; align-items: center; gap: 10px; }

  .site-header { top: 48px; height: 110px; background: var(--white); }
  .brand { position: absolute; left: 96px; top: 22px; width: 170px; display: flex; flex-direction: column; align-items: center; gap: 6px; }
  .brand .mark { width: 48px; height: 48px; background: var(--ink); }
  .brand .name { font-family: "Cinzel", serif; font-size: 17px; color: var(--ink); white-space: nowrap; }
  .main-nav a { position: absolute; top: 48px; font-family: "Cinzel", serif; font-size: 16px; font-weight: 600; color: var(--ink); text-decoration: none; }
  .main-nav a.active { color: var(--blue); border-bottom: 1px solid var(--blue); }

  .hero { top: 158px; height: 583px; }
  .hero .photo { position: absolute; inset: 0; background: linear-gradient(120deg, #3a3f6e 0%, #6d7aa6 35%, #b9c2d6 60%, #e6e9ef 80%, #9aa3bb 100%); }
  .hero .shade { position: absolute; inset: 0; background: rgba(20, 24, 60, .35); }
  .hero h1 { position: absolute; top: 192px; width: 100%; text-align: center; font-family: "Cinzel", serif; font-weight: 400; font-size: 40px; color: var(--white); }
  .hero p { position: absolute; top: 252px; width: 100%; text-align: center; font-size: 22px; color: var(--white); }

  .welcome { top: 741px; height: 518px; }
  h2.title { position: absolute; width: 100%; text-align: center; font-family: "Cinzel", serif; font-weight: 400; font-size: 40px; color: var(--ink); letter-spacing: 1px; }
  .welcome p { position: absolute; left: 118px; top: 150px; width: 964px; text-align: center; font-size: 15px; line-height: 35px; }

  .services { top: 1259px; height: 551px; background: var(--light); }
  .services .panel { position: absolute; left: 0; top: 0; width: 419px; height: 551px; background: var(--blue); color: var(--white); }
  .services .panel h2 { position: absolute; left: 90px; top: 98px; font-family: "Cinzel", serif; font-weight: 400; font-size: 36px; }
  .services .panel p { position: absolute; left: 90px; top: 166px; width: 302px; font-size: 13.5px; line-height: 31.5px; text-align: justify; }
  .card { position: absolute; top: 67px; width: 318px; height: 392px; background: var(--white); box-shadow: 0 2px 10px rgba(0,0,0,.12); text-align: center; }
  .card .icon { position: absolute; left: 109px; top: 30px; width: 100px; height: 100px; }
  .card h3 { position: absolute; left: 0; top: 138px; width: 100%; font-family: "Cinzel", serif; font-weight: 400; font-size: 26px; color: var(--ink); white-space: nowrap; }
  .card p { position: absolute; left: 22px; top: 188px; width: 274px; font-size: 15px; line-height: 32.5px; text-align: justify; text-align-last: center; }
  .card .more-link { position: absolute; left: 0; top: 327px; width: 100%; text-align: center; font-family: "Cinzel", serif; font-style: italic; font-size: 16px; color: var(--blue); text-decoration: underline; }
  .arrow { position: absolute; top: 499px; }

  .about { top: 1810px; height: 518px; }
  .about h2 { position: absolute; left: 86px; top: 88px; font-family: "Cinzel", serif; font-weight: 400; font-size: 38px; color: var(--ink); }
  .about p { position: absolute; left: 90px; top: 152px; width: 446px; font-size: 15px; line-height: 31.5px; text-align: justify; }
  .about .photo { position: absolute; left: 653px; top: 100px; width: 457px; height: 319px; background: linear-gradient(135deg, #8b97a8, #c9d1db 45%, #6a5646 80%, #3d3a3a); box-shadow: 0 4px 12px rgba(0,0,0,.25); }

  .industries { top: 2328px; height: 512px; background: var(--light); }
  .tile { position: absolute; top: 140px; height: 283px; color: var(--white); }
  .tile .label { position: absolute; bottom: 18px; width: 100%; text-align: center; font-family: "Cinzel", serif; font-size: 20px; }
  .tile .more { position: absolute; left: 64px; top: 226px; width: 121px; height: 32px; background: var(--ink); display: flex; align-items: center; justify-content: center; font-family: "Cinzel", serif; font-weight: 600; font-size: 14px; }
  .dots { position: absolute; width: 100%; display: flex; justify-content: center; gap: 8px; }
  .dots span { width: 11px; height: 11px; border-radius: 50%; background: var(--ink); }
  .dots span.on { background: var(--blue); }

  .clients { top: 2840px; height: 607px; }
  .quote { position: absolute; top: 218px; width: 315px; height: 227px; background: var(--white); border-radius: 10px; box-shadow: 0 2px 12px rgba(0,0,0,.12); text-align: center; }
  .quote.featured { background: var(--blue); color: var(--white); }
  .quote .qmark { position: absolute; left: 12px; top: -22px; font-family: Georgia, serif; font-weight: 700; font-size: 70px; line-height: 1; color: var(--blue); }
  .quote.featured .qmark { color: var(--ink); }
  .quote p { position: absolute; left: 10px; top: 30px; width: 295px; font-size: 14px; line-height: 27px; }
  .quote .person { position: absolute; left: 40px; top: 170px; display: flex; align-items: center; gap: 12px; text-align: left; }
  .quote .avatar { width: 44px; height: 44px; border-radius: 50%; background: #c9b4a2; border: 2px solid #e7e7e7; }
  .quote .who { font-family: "Cinzel", serif; font-weight: 600; font-size: 14px; color: var(--ink); }
  .quote.featured .who { color: var(--white); }
  .quote .role { font-size: 14px; }

  .contact { top: 3447px; height: 712px; }
  .field { position: absolute; border: 1px solid var(--line); background: var(--white); font-size: 19px; color: #555; padding-left: 10px; text-transform: uppercase; }

  .site-footer { top: 4159px; height: 474px; background: var(--footer); color: var(--white); }
  .site-footer h4 { position: absolute; top: 80px; font-family: "Cinzel", serif; font-weight: 400; font-size: 25px; }
  .site-footer .small { font-size: 15px; }
  .quick a { position: absolute; left: 428px; color: var(--white); text-decoration: none; font-size: 14px; }
  .social { position: absolute; top: 249px; width: 34px; height: 34px; border: 2px solid var(--white); border-radius: 50%; display: flex; align-items: center; justify-content: center; }
  .legal { position: absolute; left: 0; top: 430px; width: 100%; text-align: center; font-family: "Cinzel", serif; font-size: 16px; }
  .rule { position: absolute; left: 0; top: 392px; width: 100%; height: 1px; background: rgba(255,255,255,.25); }
</style>
</head>
<body>

<div class="topbar">
  <div class="item" style="left:90px">
    <svg width="16" height="16" viewBox="0 0 24 24" fill="#fff"><path d="M6.6 10.8a15.5 15.5 0 0 0 6.6 6.6l2.2-2.2a1 1 0 0 1 1-.25 11.4 11.4 0 0 0 3.6.57 1 1 0 0 1 1 1V20a1 1 0 0 1-1 1A17 17 0 0 1 3 4a1 1 0 0 1 1-1h3.5a1 1 0 0 1 1 1c0 1.25.2 2.45.57 3.6a1 1 0 0 1-.25 1z"/></svg>
    <span>555 210 4870</span>
  </div>
  <div class="item" style="left:260px">
    <svg width="18" height="14" viewBox="0 0 24 18" fill="none" stroke="#fff" stroke-width="2"><rect x="1" y="1" width="22" height="16" rx="2"/><path d="M1 2l11 8 11-8"/></svg>
    <span>info@MarbeckPartners.com</span>
  </div>
</div>

<header class="site-header">
  <div class="brand"><div class="mark"></div><div class="name">Marbeck Partners</div></div>
  <nav class="main-nav">
    <a class="active" href="#" style="left:419px">Home</a>
    <a href="#" style="left:507px">About Us</a>
    <a href="#" style="left:628px">Services</a>
    <a href="#" style="left:739px">Industries</a>
    <a href="#" style="left:876px">Our Success</a>
    <a href="#" style="left:1027px">Contact</a>
  </nav>
</header>

<section class="hero">
  <div class="photo" role="img" aria-label="Overhead view of business people reviewing financial charts at a desk"></div>
  <div class="shade"></div>
  <h1>"Does your business have an exit plan?"</h1>
  <p>Let us help you with a completely impartial, no obligation assessment</p>
  <a class="btn" href="#" style="left:482px;top:306px;width:234px;height:74px;font-size:26px">Contact Us</a>
</section>

<section class="welcome">
  <h2 class="title" style="top:80px">Welcome to Marbeck Partners</h2>
  <p>Lorem ipsum dolor sit amet, consectetur adipiscing elit, sed do eiusmod tempor incididunt ut labore et dolore magna aliqua. Ut enim ad minim veniam, quis nostrud exercitation ullamco laboris nisi ut aliquip ex ea commodo consequat. Duis aute irure dolor in reprehenderit in voluptate velit esse cillum dolore eu fugiat nulla pariatur.Excepteur sint occaecat cupidatat non proident, sunt in culpa qui officia deserunt mollit anim id est laborumQuis autem vel eum iure reprehenderit qui in ea voluptate velit esse quam nihil molestiae consequatur, vel illum qui dolorem eum fugiat quo voluptas nulla pariatur</p>
  <a class="btn" href="#" style="left:482px;top:353px;width:234px;height:66px;font-size:24px">Read More</a>
</section>

<section class="services">
  <div class="panel">
    <h2>Services</h2>
    <p>Lorem ipsum dolor sit amet, consectetur adipiscing elit, sed do eiusmod tempor ididunt ut labore et dolore magna aliqua. Ut enim ad minim veniam, quis nostrud exercitation lamco laboris nisi ut aliquip ex ea commodo uat.</p>
    <a class="btn" href="#" style="left:90px;top:387px;width:178px;height:59px;font-size:20px">View More</a>
  </div>
  <div class="card" style="left:459px">
    <svg class="icon" viewBox="0 0 100 100" fill="none" stroke="#1e96d3" stroke-width="3" stroke-linejoin="round">
      <rect x="18" y="44" width="38" height="50" rx="3"/>
      <rect x="24" y="50" width="26" height="10"/>
      <path d="M26 68h4M36 68h4M46 68h4M26 77h4M36 77h4M46 77h4M26 86h4M36 86h4M46 86h4"/>
      <circle cx="66" cy="30" r="20"/>
      <path d="M72 22c-2-3-12-3-12 2s12 3 12 9-10 5-12 2M66 16v4M66 41v4"/>
      <path d="M60 60h28v34H60"/>
      <path d="M66 70h16M66 78h16M66 86h10"/>
    </svg>
    <h3>Accountant</h3>
    <p>Lorem ipsum dolor sit amet, consectetur adipiscing elit, sed do eiusmod tempor incididunt ut labore et dolore magna aliqua.</p>
    <a class="more-link" href="#">View More →</a>
  </div>
  <div class="card" style="left:790px">
    <svg class="icon" viewBox="0 0 100 100" fill="none" stroke="#1e96d3" stroke-width="3" stroke-linejoin="round">
      <path d="M8 32L44 12l36 20z"/>
      <path d="M12 36h64"/>
      <path d="M18 42v26M30 42v26M42 42v26M54 42v26M66 42v26"/>
      <path d="M10 74h56M6 82h58"/>
      <circle cx="76" cy="74" r="18"/>
      <path d="M66 70a11 11 0 0 1 19-5l2 2M86 78a11 11 0 0 1-19 5l-2-2"/>
      <path d="M87 60v7h-7M65 88v-7h7"/>
    </svg>
    <h3>Investment Banker</h3>
    <p>Lorem ipsum dolor sit amet, consectetur adipiscing elit, sed do eiusmod tempor incididunt ut labore et dolore magna aliqua.</p>
    <a class="more-link" href="#">View More →</a>
  </div>
  <svg class="arrow" style="left:757px" width="22" height="22" viewBox="0 0 22 22"><circle cx="11" cy="11" r="10" fill="#111"/><path d="M13 6l-5 5 5 5M8 11h8" stroke="#fff" stroke-width="2.2" fill="none"/></svg>
  <svg class="arrow" style="left:793px" width="22" height="22" viewBox="0 0 22 22"><circle cx="11" cy="11" r="10" fill="#111"/><path d="M9 6l5 5-5 5M14 11H6" stroke="#fff" stroke-width="2.2" fill="none"/></svg>
</section>

<section class="about">
  <h2>About Us</h2>
  <p>Lorem ipsum dolor sit amet, consectetur adipiscing elit, sed do eiusmod tempor incididunt ut labore et dolore magna aliqua. Ut enim ad minim veniam, quis nostrud exercitation ullamco laboris nisi ut aliquip ex ea commodo consequat. Duis aute irure dolor in reprehenderit in voluptate velit esse cillum dolore eu fugiat nulla pariatur</p>
  <a class="btn" href="#" style="left:90px;top:359px;width:178px;height:58px;font-size:20px">Read More</a>
  <div class="photo" role="img" aria-label="Business team meeting around a conference table"></div>
</section>

<section class="industries">
  <h2 class="title" style="top:45px">Industries</h2>
  <div class="tile" style="left:86px;width:249px;background:linear-gradient(160deg,#6b5a4c,#b7a08a 55%,#4b6a78)" role="img" aria-label="Healthcare worker with a patient"><div class="label">Healthcare</div></div>
  <div class="tile" style="left:345px;width:247px;background:linear-gradient(160deg,#2f5f8a,#6fa4c9 50%,#2b7fb8)" role="img" aria-label="Scientist examining a sample in a laboratory"><div class="label">Life Sciences</div></div>
  <div class="tile" style="left:603px;width:248px;background:linear-gradient(160deg,#5b5f66,#9a9ea4 50%,#6e7076)" role="img" aria-label="Insurance agreement being signed">
    <div class="label" style="bottom:68px">Insurance</div><div class="more">View More</div>
  </div>
  <div class="tile" style="left:860px;width:248px;background:linear-gradient(160deg,#c9c6c0,#8f8a84 50%,#d8d6d2)" role="img" aria-label="Public sector office worker"><div class="label">Public Sector</div></div>
  <div class="dots" style="top:467px"><span></span><span></span><span></span><span class="on"></span><span></span></div>
</section>

<section class="clients">
  <h2 class="title" style="top:92px">What Clients Say</h2>
  <div class="quote" style="left:101px">
    <div class="qmark">“</div>
    <p>"Lorem ipsum dolor sit amet, consectetur adipiscing elit, sed do eiusmod tempor incididunt ut labore et dolore magna aliqua. Ut enim adminim veniam, quis nostrud exercitation"</p>
    <div class="person"><div class="avatar" role="img" aria-label="Client portrait"></div><div><div class="who">Clara Vance</div><div class="role">Client Customer</div></div></div>
  </div>
  <div class="quote featured" style="left:439px">
    <div class="qmark">“</div>
    <p>"Lorem ipsum dolor sit amet, consectetur adipiscing elit, sed do eiusmod tempor incididunt ut labore et dolore magna aliqua. Ut enim adminim veniam, quis nostrud exercitation"</p>
    <div class="person"><div class="avatar" role="img" aria-label="Client portrait"></div><div><div class="who">Owen Hale</div><div class="role">Client Customer</div></div></div>
  </div>
  <div class="quote" style="left:775px">
    <div class="qmark">“</div>
    <p>"Lorem ipsum dolor sit amet, consectetur adipiscing elit, sed do eiusmod tempor incididunt ut labore et dolore magna aliqua. Ut enim adminim veniam, quis nostrud exercitation"</p>
    <div class="person"><div class="avatar" role="img" aria-label="Client portrait"></div><div><div class="who">Peter Lasko</div><div class="role">Client Customer</div></div></div>
  </div>
  <div class="dots" style="top:494px"><span></span><span></span><span></span><span class="on"></span><span></span></div>
</section>

<section class="contact">
  <h2 class="title" style="top:50px">Contact Us</h2>
  <div class="field" style="left:92px;top:171px;width:316px;height:74px;line-height:74px">Enter Name</div>
  <div class="field" style="left:437px;top:171px;width:317px;height:74px;line-height:74px">Enter Email</div>
  <div class="field" style="left:784px;top:171px;width:317px;height:74px;line-height:70px">Phone</div>
  <div class="field" style="left:86px;top:282px;width:1019px;height:261px;padding:18px 22px">Messages</div>
  <a class="btn" href="#" style="left:507px;top:592px;width:178px;height:59px;font-size:22px">Submit</a>
</section>

<footer class="site-footer">
  <h4 style="left:90px">Contact Us</h4>
  <svg class="abs" style="left:92px;top:145px" width="18" height="13" viewBox="0 0 24 18" fill="none" stroke="#fff" stroke-width="2"><rect x="1" y="1" width="22" height="16" rx="2"/><path d="M1 2l11 8 11-8"/></svg>
  <div class="abs small" style="left:126px;top:139px;line-height:23px">Email:<br>info@Marbeck Partners</div>
  <a class="social" href="#" style="left:94px" aria-label="Social profile link"><svg width="16" height="16" viewBox="0 0 16 16" fill="none" stroke="#fff" stroke-width="1.8"><circle cx="4" cy="8" r="2"/><circle cx="12" cy="3.5" r="2"/><circle cx="12" cy="12.5" r="2"/><path d="M5.8 7l4.4-2.5M5.8 9l4.4 2.5"/></svg></a>
  <a class="social" href="#" style="left:136px" aria-label="Social profile link"><svg width="16" height="16" viewBox="0 0 16 16" fill="none" stroke="#fff" stroke-width="1.8"><circle cx="4" cy="8" r="2"/><circle cx="12" cy="3.5" r="2"/><circle cx="12" cy="12.5" r="2"/><path d="M5.8 7l4.4-2.5M5.8 9l4.4 2.5"/></svg></a>
  <a class="social" href="#" style="left:176px" aria-label="Social profile link"><svg width="16" height="16" viewBox="0 0 16 16" fill="none" stroke="#fff" stroke-width="1.8"><circle cx="4" cy="8" r="2"/><circle cx="12" cy="3.5" r="2"/><circle cx="12" cy="12.5" r="2"/><path d="M5.8 7l4.4-2.5M5.8 9l4.4 2.5"/></svg></a>

  <h4 style="left:426px">Quick Links</h4>
  <div class="quick">
    <a href="#" style="top:142px">Home</a>
    <a href="#" style="top:178px">About Us</a>
    <a href="#" style="top:214px">Services</a>
    <a href="#" style="top:250px">Industries</a>
    <a href="#" style="top:286px">Our Success</a>
    <a href="#" style="top:322px">Contact</a>
  </div>

  <h4 style="left:738px">Sign Up</h4>
  <div class="abs" style="left:735px;top:146px;font-size:13px">Alternatively You Can Fill In The Following Contact Form:</div>
  <div class="abs" style="left:735px;top:186px;width:359px;height:44px;border:1px solid #fff;font-size:12px;line-height:42px;padding-left:14px">E - Mail</div>
  <div class="abs serif" style="left:735px;top:259px;width:236px;height:42px;border:1px solid #fff;text-align:center;line-height:40px;font-size:18px">Submit</div>

  <div class="rule"></div>
  <div class="legal">(c) 2020 Marbeck Partners | All Rights Reserved | Terms and Conditions</div>
</footer>

</body>
</html>
```